Rollers & Glides.com

Vertical Business Card with focus on branding with our icon. Information on card will be logo, persons name, position, phone number, email address and website. Use the the name Marcus Tilden, position President, phone number 555.214.8890, email Marcus@rollersandglides.com, website www.rollersandglides.com.

```html
<!DOCTYPE html>
<html lang="en">
<head>
<meta charset="UTF-8">
<title>Rollers &amp; Glides.com — Business Card</title>
<link href="https://fonts.googleapis.com/css2?family=Roboto:wght@400;700&family=Roboto+Condensed:wght@400&display=swap" rel="stylesheet">
<style>
  :root {
    --brand-blue: #335fab;
    --ink: #1d1d1d;
    --paper: #ffffff;
    --backdrop: #b8b8b8;
  }
  * { margin: 0; padding: 0; box-sizing: border-box; }
  html, body {
    width: 1200px; height: 801px; overflow: hidden;
    background: var(--backdrop);
  }
  .card {
    position: absolute;
    top: 274px;
    width: 443px; height: 263px;
    overflow: hidden;
  }
  .card--front { left: 153px; background: var(--paper); }
  .card--back { left: 625px; background: var(--brand-blue); }

  .wordmark {
    font-family: "Roboto Condensed", sans-serif;
    font-weight: 400;
    font-size: 24px;
    letter-spacing: 0.5px;
    white-space: nowrap;
  }
  .card--front .wordmark {
    position: absolute; left: 23px; top: 44px;
    color: var(--brand-blue);
  }
  .brand-disc {
    position: absolute;
    left: 226px; top: 51px;
    width: 220px; height: 220px;
    border-radius: 50%;
    background: var(--brand-blue);
  }
  .person {
    position: absolute; left: 25px; top: 134px;
    font-family: "Roboto", sans-serif;
  }
  .person__name {
    font-weight: 700; font-size: 16px;
    color: var(--brand-blue); text-transform: uppercase;
    line-height: 18px;
  }
  .person__role {
    font-size: 13px; color: var(--ink); line-height: 15px;
  }
  .contact {
    position: absolute; left: 24px; top: 185px;
    list-style: none;
    font-family: "Roboto", sans-serif;
    font-size: 12.5px; color: var(--ink);
  }
  .contact li {
    display: flex; align-items: center;
    height: 15.7px;
  }
  .contact svg {
    width: 11px; height: 11px; margin-right: 5px;
    fill: var(--brand-blue);
    flex-shrink: 0;
  }
  .contact .domain { color: var(--brand-blue); }

  .card--back .brand-dot {
    position: absolute; left: 191px; top: 78px;
    width: 60px; height: 60px; border-radius: 50%;
    background: var(--paper);
  }
  .card--back .wordmark {
    position: absolute; left: 0; right: 0; top: 164px;
    text-align: center; color: var(--paper);
  }
</style>
</head>
<body>
  <section class="card card--front">
    <div class="wordmark">Rollers &amp; Glides.com</div>
    <div class="brand-disc"></div>
    <div class="person">
      <div class="person__name">Marcus Tilden</div>
      <div class="person__role">President</div>
    </div>
    <ul class="contact">
      <li>
        <svg viewBox="0 0 24 24" aria-hidden="true"><path d="M6.6 10.8a15.1 15.1 0 0 0 6.6 6.6l2.2-2.2a1 1 0 0 1 1-.25 11.4 11.4 0 0 0 3.6.57 1 1 0 0 1 1 1V20a1 1 0 0 1-1 1A17 17 0 0 1 3 4a1 1 0 0 1 1-1h3.5a1 1 0 0 1 1 1c0 1.25.2 2.45.57 3.57a1 1 0 0 1-.25 1z"/></svg>
        555.214.8890
      </li>
      <li>
        <svg viewBox="0 0 24 24" aria-hidden="true"><path d="M2 5h20v14H2zm2 2v.5l8 5 8-5V7l-8 5z"/></svg>
        Marcus@rollersandglides.com
      </li>
      <li>
        <svg viewBox="0 0 24 24" aria-hidden="true"><path d="M12 2a10 10 0 1 0 0 20 10 10 0 0 0 0-20zm0 2c.9 0 2.2 1.8 2.7 5H9.3C9.8 5.8 11.1 4 12 4zM4.3 11h3a17 17 0 0 0 0 2h-3a8 8 0 0 1 0-2zm5 0h5.4a15 15 0 0 1 0 2H9.3a15 15 0 0 1 0-2zm7.4 0h3a8 8 0 0 1 0 2h-3a17 17 0 0 0 0-2zM9.3 15h5.4c-.5 3.2-1.8 5-2.7 5s-2.2-1.8-2.7-5z"/></svg>
        <span>www.<span class="domain">rollersandglides</span>.com</span>
      </li>
    </ul>
  </section>

  <section class="card card--back">
    <div class="brand-dot"></div>
    <div class="wordmark">Rollers &amp; Glides.com</div>
  </section>
</body>
</html>
```